Business card design for engineering firm specializing in defense industry.

We need a professional business card design. Something simple but stands out. We are an engineering company specializing in composites in the defense industry.
Industry/Entity Type
Defense
Contact Information for Business Card
A simple black business card with the Varlonix yellow color is what we had in mind but open for other designs.
Colors
ffc214

```html
<!DOCTYPE html>
<html lang="en">
<head>
<meta charset="utf-8">
<title>Varlonix Business Card</title>
<link rel="stylesheet" href="https://fonts.googleapis.com/css2?family=Arimo:wght@400;700&display=swap">
<style>
  :root {
    --stage: #2b2b2b;
    --card: #1b1b1b;
    --card-edge: #242424;
    --ink: #ffffff;
    --accent: #ffc214;
    --muted: #e8e8e8;
  }
  * { box-sizing: border-box; margin: 0; padding: 0; }
  html, body {
    width: 1200px; height: 1189px; overflow: hidden;
    background: var(--stage);
    font-family: "Arimo", Arial, sans-serif;
  }
  .stage {
    position: relative; width: 1200px; height: 1189px;
    display: flex; flex-direction: column; align-items: center;
    justify-content: center; gap: 60px;
  }
  .card {
    position: relative; width: 900px; height: 514px;
    background: var(--card);
    border: 1px solid var(--card-edge);
    border-radius: 34px;
    box-shadow: 0 18px 40px rgba(0,0,0,.55);
    overflow: hidden;
  }
  .wordmark {
    display: flex; align-items: center; gap: 18px;
    color: var(--ink); font-weight: 700; letter-spacing: 1px;
  }
  .wordmark__square { background: var(--accent); flex: none; }
  .card--front .wordmark {
    position: absolute; left: 50%; top: 50%;
    transform: translate(-50%, -50%); font-size: 96px;
  }
  .card--front .wordmark__square { width: 54px; height: 54px; }
  .card--back .wordmark {
    position: absolute; left: 80px; top: 50%;
    transform: translateY(-50%); font-size: 62px;
  }
  .card--back .wordmark__square { width: 36px; height: 36px; }
  .divider {
    position: absolute; left: 470px; top: 150px;
    width: 2px; height: 214px; background: var(--accent);
  }
  .contact {
    position: absolute; left: 520px; top: 150px; color: var(--muted);
  }
  .contact__name { font-size: 32px; font-weight: 700; color: var(--ink); line-height: 1; }
  .contact__title { font-size: 22px; color: var(--accent); margin-top: 4px; }
  .contact__list { list-style: none; margin-top: 22px; }
  .contact__item {
    display: flex; align-items: center; gap: 14px;
    font-size: 24px; line-height: 36px;
  }
  .contact__icon { width: 20px; height: 20px; flex: none; }
  .contact__highlight { color: var(--accent); }
</style>
</head>
<body>
<main class="stage">
  <section class="card card--front" aria-label="Card front">
    <div class="wordmark"><span class="wordmark__square"></span>Varlonix</div>
  </section>

  <section class="card card--back" aria-label="Card back">
    <div class="wordmark"><span class="wordmark__square"></span>Varlonix</div>
    <div class="divider"></div>
    <div class="contact">
      <p class="contact__name">Daniel Reyes</p>
      <p class="contact__title">President</p>
      <ul class="contact__list">
        <li class="contact__item">
          <svg class="contact__icon" viewBox="0 0 20 20"><rect x="5" y="2" width="10" height="16" rx="2" fill="none" stroke="var(--accent)" stroke-width="2"/></svg>
          555-214-0387
        </li>
        <li class="contact__item">
          <svg class="contact__icon" viewBox="0 0 20 20"><path d="M2 7c0-3 16-3 16 0v2h-4V7H6v2H2z" fill="var(--accent)"/><rect x="4" y="10" width="12" height="7" rx="1" fill="var(--accent)"/></svg>
          555-214-0387
        </li>
        <li class="contact__item">
          <svg class="contact__icon" viewBox="0 0 20 20"><rect x="1" y="4" width="18" height="12" fill="var(--accent)"/><path d="M1 4l9 7 9-7" fill="none" stroke="var(--card)" stroke-width="1.6"/></svg>
          info@varlonixmail.com
        </li>
        <li class="contact__item">
          <svg class="contact__icon" viewBox="0 0 20 20"><circle cx="10" cy="10" r="8" fill="var(--accent)"/><path d="M2 10h16M10 2v16M4.5 5.5h11M4.5 14.5h11" stroke="var(--card)" stroke-width="1.2" fill="none"/><ellipse cx="10" cy="10" rx="3.5" ry="8" fill="none" stroke="var(--card)" stroke-width="1.2"/></svg>
          <span>www.<span class="contact__highlight">varlonixweb</span>.com</span>
        </li>
      </ul>
    </div>
  </section>
</main>
</body>
</html>
```